Harbor Crest Renewal Business Cards

We need a sleek and sexy business card design

Contact Information for Business Card

Name, address, phone number, email. Vincent Morrasco 482 Pellham Street Suite 200C Holtsville NY 11958 (631)555-0174 Also a second version with the name Derek Halvorn

```html
<!DOCTYPE html>
<html lang="en">
<head>
<meta charset="utf-8">
<title>Harbor Crest Renewal – Business Cards</title>
<link rel="stylesheet" href="https://fonts.googleapis.com/css2?family=Michroma&family=Arimo:wght@400&family=Montserrat:wght@600&display=swap">
<style>
  :root {
    --backdrop: #a3a3a3;
    --card: #ffffff;
    --brand-blue: #0d4a9a;
    --brand-orange: #d2420f;
    --ink: #1e1e1e;
    --rule: #8a8a8a;
    --ghost-light: #f6f6f6;
    --ghost-dark: #e6e6e6;
  }
  html, body {
    margin: 0;
    width: 1200px;
    height: 1200px;
    overflow: hidden;
    background: var(--backdrop);
  }
  .stage {
    position: relative;
    width: 1200px;
    height: 1200px;
  }
  .card {
    position: absolute;
    top: 303px;
    width: 369px;
    height: 593px;
    background: var(--card);
    box-shadow: 3px 4px 6px rgba(0,0,0,0.45);
    overflow: hidden;
  }
  .card--front { left: 200px; }
  .card--back  { left: 599px; width: 364px; }

  .card__backdrop {
    position: absolute;
    left: 52px;
    top: 88px;
    right: 0;
    bottom: 0;
    background: linear-gradient(160deg, var(--ghost-dark) 0%, var(--ghost-light) 60%, rgba(255,255,255,0) 100%);
  }

  .brand {
    position: absolute;
    left: 0;
    right: 0;
    display: flex;
    flex-direction: column;
    align-items: center;
  }
  .brand__mark {
    width: 44px;
    height: 44px;
    background: var(--brand-orange);
    margin-bottom: 14px;
  }
  .brand__name {
    font-family: "Montserrat", sans-serif;
    font-weight: 600;
    color: var(--brand-blue);
    font-size: 32px;
    letter-spacing: 0.5px;
    text-align: center;
    line-height: 1.1;
  }
  .card--front .brand { top: 408px; }
  .card--back .brand  { top: 140px; }

  .contact {
    position: absolute;
    top: 387px;
    left: 0;
    right: 0;
    text-align: center;
    font-family: "Arimo", sans-serif;
    color: var(--ink);
    font-size: 16px;
  }
  .contact__name {
    font-family: "Michroma", sans-serif;
    font-size: 19px;
    margin: 0;
    font-weight: 400;
  }
  .contact__first { color: var(--brand-blue); }
  .contact__last  { color: var(--brand-orange); }
  .contact__rule {
    width: 54px;
    height: 1px;
    background: var(--rule);
    margin: 12px auto 13px;
    border: 0;
  }
  .contact p { margin: 0; line-height: 22px; }
</style>
</head>
<body>
  <main class="stage">
    <section class="card card--front" aria-label="Card front">
      <div class="card__backdrop" role="img" aria-label="Faint oversized brand emblem in light grey"></div>
      <div class="brand">
        <span class="brand__mark"></span>
        <span class="brand__name">Harbor Crest<br>Renewal</span>
      </div>
    </section>

    <section class="card card--back" aria-label="Card back">
      <div class="brand">
        <span class="brand__mark"></span>
        <span class="brand__name">Harbor Crest<br>Renewal</span>
      </div>
      <div class="contact">
        <h1 class="contact__name"><span class="contact__first">Vincent</span> <span class="contact__last">Morrasco</span></h1>
        <hr class="contact__rule">
        <p>(631)555-0174</p>
        <p>vincent@mailbox.com</p>
        <hr class="contact__rule">
        <p>482 Pellham Street</p>
        <p>Suite 200C Holtsville NY 11958</p>
      </div>
    </section>
  </main>
</body>
</html>
```